Birchfield Dental Care Stationery

create stationery, business cards and envelops for business. Use current logo on website but open to new fonts for the business name. Business name is Birchfield Dental Care, would like below the name added "Cosmetic - Family - Implants" Website is www.birchfielddentalcareQX.example. I would like to have modern look, clean, and professional. The water mark of the logo is a great thing to ad as well.

Target Market(s)

General public, Families, Cosmetic, Implant

Industry/Entity Type

Dental

Font styles to use
Sans Serif

Colors
9bcb3c
000000
757575
c9c9c9

Requirements
Must have
• Would like to see different versions of the current logo. Improvements, color, sytle, and class.
Nice to have
• current font has double "oo" in the Birchfield logo, does not need to have with new logo.

```html
<!DOCTYPE html>
<html lang="en">
<head>
<meta charset="utf-8">
<title>Birchfield Dental Care Stationery</title>
<link href="https://fonts.googleapis.com/css2?family=Lato:wght@400;700&display=swap" rel="stylesheet">
<style>
:root{
  --backdrop:#3a1410;
  --blue:#1177c0;
  --green:#8dc63f;
  --white:#ffffff;
  --paper:#ffffff;
  --ink:#555555;
  --faint:#e3e3e3;
  --faint-blue:#0f69ab;
}
*{box-sizing:border-box;margin:0;padding:0}
html,body{width:1200px;height:941px;overflow:hidden}
body{background:var(--backdrop);font-family:'Lato',sans-serif;position:relative}
.piece{position:absolute;overflow:hidden;background:var(--paper)}
.piece svg.art{position:absolute;inset:0;width:100%;height:100%}
.mark{position:absolute;text-align:center;font-family:'Lato',sans-serif;font-weight:700;line-height:1.05}
.mark .dot{display:block;margin:0 auto 4px;border-radius:50%}
.mark.on-white{color:var(--blue)}
.mark.on-white .dot{background:var(--green)}
.mark.on-blue{color:var(--white)}
.mark.on-blue .dot{background:var(--green)}
.contact{position:absolute;font-size:7px;line-height:1.45;color:#333}
.contact .ico{display:inline-block;width:5px;height:5px;border-radius:50%;background:var(--blue);margin-right:4px;vertical-align:middle}
.divider{position:absolute;width:1px;background:#c9d7e6}

.letterhead{left:52px;top:63px;width:353px;height:498px}
.folder{left:434px;top:63px;width:393px;height:532px;background:var(--blue)}
.card-front{left:859px;top:157px;width:302px;height:179px;border-radius:14px}
.card-back{left:859px;top:371px;width:302px;height:173px;border-radius:14px;background:var(--blue)}
.envelope-front{left:52px;top:631px;width:536px;height:226px}
.envelope-back{left:617px;top:631px;width:517px;height:225px;background:linear-gradient(#ffffff,#f3f3f3)}

.tagline{position:absolute;left:0;right:0;text-align:center;color:var(--white);font-size:8px}
.card-name{position:absolute;left:190px;top:24px;color:var(--green);font-weight:700;font-size:11px}
.card-front .contact{color:var(--white);font-size:6.5px;left:190px}
.card-front .contact .ico{background:var(--green)}
.env-address{position:absolute;left:188px;top:40px;font-size:9px;line-height:1.5;color:#555}
</style>
</head>
<body>

<section class="piece letterhead">
  <svg class="art" viewBox="0 0 353 498" preserveAspectRatio="none" aria-hidden="true">
    <circle cx="262" cy="398" r="96" fill="none" stroke="var(--faint)" stroke-width="8"/>
    <path d="M0 0H84Q28 250 96 498H0Z" fill="var(--blue)"/>
    <path d="M88 0Q36 250 104 498H110Q46 250 94 0Z" fill="var(--green)"/>
  </svg>
  <div class="mark on-white" style="left:92px;top:22px;width:96px;font-size:13px">
    <span class="dot" style="width:22px;height:22px"></span>Birchfield<br>Dental Care
  </div>
  <div class="divider" style="left:195px;top:24px;height:54px"></div>
  <div class="contact" style="left:202px;top:26px">
    <span class="ico"></span>2150 N Alder Ln<br>
    &nbsp;&nbsp;&nbsp;Fairview, QX 00123-4567<br>
    <span class="ico"></span>555-014-2210<br>
    <span class="ico"></span>hello@birchfielddental.example<br>
    <span class="ico"></span>www.birchfielddentalcareQX.example
  </div>
</section>

<section class="piece folder">
  <svg class="art" viewBox="0 0 393 532" aria-hidden="true">
    <circle cx="255" cy="335" r="128" fill="none" stroke="var(--faint-blue)" stroke-width="10"/>
  </svg>
  <div class="mark on-blue" style="left:0;right:0;top:46px;font-size:27px">
    <span class="dot" style="width:60px;height:60px;margin-bottom:12px"></span>Birchfield<br>Dental Care
  </div>
  <p class="tagline" style="top:465px">Cosmetic - Family - Implant</p>
  <p class="tagline" style="top:477px">www.birchfielddentalcareQX.example</p>
</section>

<section class="piece card-front">
  <svg class="art" viewBox="0 0 302 179" preserveAspectRatio="none" aria-hidden="true">
    <path d="M182 0Q112 90 182 179H302V0Z" fill="var(--blue)"/>
    <path d="M174 0Q106 90 174 179H168Q98 90 168 0Z" fill="var(--green)"/>
  </svg>
  <div class="mark on-white" style="left:18px;top:46px;width:100px;font-size:14px">
    <span class="dot" style="width:26px;height:26px"></span>Birchfield<br>Dental Care
  </div>
  <p class="card-name">Daniel R. Marsh DDS</p>
  <div class="contact" style="top:58px">
    <span class="ico"></span>2150 N Alder Ln<br>
    &nbsp;&nbsp;&nbsp;Fairview, QX<br>
    &nbsp;&nbsp;&nbsp;00123-4567
  </div>
  <div class="contact" style="top:99px">
    <span class="ico"></span>555-014-2210<br>
    <span class="ico"></span>555-014-2211<br>
    <span class="ico"></span>hello@birchfielddental.example<br>
    <span class="ico"></span>www.birchfielddentalcareQX.example
  </div>
</section>

<section class="piece card-back">
  <svg class="art" viewBox="0 0 302 173" aria-hidden="true">
    <circle cx="80" cy="92" r="72" fill="none" stroke="var(--faint-blue)" stroke-width="7"/>
  </svg>
  <div class="mark on-blue" style="left:95px;top:30px;width:110px;font-size:15px">
    <span class="dot" style="width:28px;height:28px"></span>Birchfield<br>Dental Care
  </div>
  <p class="tagline" style="top:126px;font-size:7.5px">Cosmetic - Family - Implant</p>
</section>

<section class="piece envelope-front">
  <svg class="art" viewBox="0 0 536 226" preserveAspectRatio="none" aria-hidden="true">
    <circle cx="455" cy="100" r="74" fill="none" stroke="var(--faint)" stroke-width="7"/>
    <path d="M0 0H50Q18 113 52 226H0Z" fill="var(--blue)"/>
    <path d="M54 0Q22 113 56 226H60Q28 113 58 0Z" fill="var(--green)"/>
  </svg>
  <div class="mark on-white" style="left:62px;top:30px;width:100px;font-size:14px">
    <span class="dot" style="width:26px;height:26px"></span>Birchfield<br>Dental Care
  </div>
  <div class="divider" style="left:174px;top:28px;height:80px"></div>
  <p class="env-address">2150 N Alder Ln,<br>Fairview,<br>QX 00123-4567</p>
</section>

<section class="piece envelope-back">
  <svg class="art" viewBox="0 0 517 225" aria-hidden="true">
    <path d="M0 0H517V40Q517 60 497 60H78Q58 60 50 40L40 20H0Z" fill="var(--blue)"/>
    <path d="M0 0V20H40Z" fill="var(--blue)"/>
    <circle cx="259" cy="32" r="18" fill="var(--green)"/>
  </svg>
</section>

</body>
</html>
```